依頼詳細
上記ポータルサイトのWebページデザインを依頼いたします。
両企業のHPをご覧になって企業色をご理解頂き、違和感の無い雰囲気作りを希望いたします。
メインタイトルである「ハルタカグループは子育て支援を応援しています。」は固定でお願いいたします。ロゴマーク等は添付ファイルのものをご利用ください。
尚、添付ファイルはダミーデザインです。このデザインに固執しない自由な発想で結構です。
デザイン作成にあたりスマートホンでの閲覧も考慮頂きたく思います。
サイトURL
http://www.hinata-nestlu.jp
ページ数
1ページ
希望イメージ
シンプル 複雑
単色 カラフル
暗い 明るい
日常 高級
遊び心 厳粛
未来的 伝統的
女性的 男性的
希望する色
赤系、青系、水色系、黄・オレンジ系、同社はブルー・赤・黄色の三色を基本企業色としております。
納品ファイル
• イラストレーター形式 (.ai)
補足説明
子育てに関係するサイトなので、対象となる人物像は20代以降の幅広い年齢層であることをご留意いただきたく思います。
[3/4追記]
いつもお世話になります。本案件につきましてご提案をお考え頂いております方にご案内いたします。ご提案の締切日の変更ではございませんが、クライアントに対して中間報告をしたいと存じます。つきましてはご提案頂ける状態になった方はお早めにご提案頂けましたら幸いでございます。3/12・13と土日も挟みますので、3/10の状況を報告したいと考えております。もちろん3/14の締切は変更ございませんし、早くご提案頂くことでの優遇もございませんが、当方でのプレゼン作業もございますのでご理解頂けましたら幸いでございます。ご無理申し上げますが宜しくお願いいたします。
■ 選んだ理由

この度は本案件に対しまして多数のご提案を頂き誠にありがとうございました。クライアントとの協議の結果pelirund4様のご提案デザインを採用とさせていただきます。選定方法は関連企業を含む100余名の女性によるアンケートを含む審査によります。クライアントのホームページとの親和性も問題なく、女性に好感を持たれる良好なデザインであった考えます。

■ 提案者全員のお礼・コメント

殆どの応募案はどれを採用としても問題が無いほど僅差であり、よく吟味されたデザインであったと思います。残念ながら採用とならなかった応募者の方々にも心から感謝申し上げます。またの機会がございましたら何卒宜しくお願い申し上げます。

```html
<!DOCTYPE html>
<html lang="ja">
<head>
<meta charset="utf-8">
<title>ハルタカグループ 子育て支援ポータルサイト</title>
<link href="https://fonts.googleapis.com/css2?family=Noto+Sans+JP:wght@400;700&display=swap" rel="stylesheet">
<style>
:root{
  --brand-red:#d7262d;
  --brand-blue:#1f5fae;
  --text-blue:#2a6cc0;
  --footer-blue:#1c4f9c;
  --footer-dark:#143c7a;
  --ink:#444;
  --muted:#777;
  --line:#d9dfe8;
  --page:#f1f2f4;
  --panel:#ffffff;
}
*{margin:0;padding:0;box-sizing:border-box}
html,body{width:838px;height:1200px;overflow:hidden}
body{font-family:"Noto Sans JP",sans-serif;background:var(--page);color:var(--ink);position:relative}
.site-header{height:60px;background:var(--panel);display:flex;justify-content:space-between;align-items:center;padding:0 112px;border-bottom:1px solid var(--line)}
.brand{display:flex;align-items:center;gap:10px}
.brand-mark{display:flex;align-items:center;gap:5px;color:var(--brand-red);font-weight:700;font-size:15px}
.brand-mark::before{content:"";width:12px;height:12px;background:var(--brand-red)}
.brand-title{color:var(--brand-blue);font-size:13px;font-weight:700}
.header-tools{display:flex;flex-direction:column;align-items:flex-end;gap:6px;font-size:9px;color:var(--muted)}
.group-links{display:flex;gap:10px}
.group-links span::before{content:"▶";color:var(--brand-blue);font-size:7px;margin-right:3px}
.font-size{display:flex;align-items:center;gap:3px}
.font-size b{display:inline-block;width:16px;height:14px;line-height:14px;text-align:center;background:#e4e8ee;color:var(--ink);font-weight:400}
.font-size b.on{background:var(--brand-blue);color:#fff}
.hero{position:relative;height:318px}
.hero-photo{position:absolute;inset:0;background:linear-gradient(180deg,#a9d3f0 0%,#d4ebf7 38%,#c7dda0 58%,#8fb857 80%,#7aa64a 100%)}
.hero-copy{position:absolute;left:112px;top:125px;color:var(--text-blue);font-weight:700;font-size:19px;line-height:1.7;text-shadow:0 0 6px #fff,0 0 3px #fff}
.content{width:628px;margin:0 auto;background:var(--panel);padding:22px 0 12px}
.section-title{font-size:12px;font-weight:700;color:var(--brand-blue);border-bottom:2px solid var(--brand-blue);padding:0 0 4px 10px;margin:0 0 10px}
.section-title span{border-left:4px solid var(--brand-blue);padding-left:6px}
.link-list{list-style:none}
.link-item{display:flex;gap:18px;padding:10px 10px;border-bottom:1px dotted var(--line);height:103px}
.link-banner{width:228px;height:80px;flex:none;border:1px solid var(--line)}
.b1{background:linear-gradient(135deg,#fff6e0,#f7d27a)}
.b2{background:linear-gradient(135deg,#fff5d9,#f3b74a)}
.b3{background:linear-gradient(135deg,#ffeef0,#e87c8c)}
.b4{background:linear-gradient(135deg,#e8f6fb,#7fc6e4)}
.b5{background:linear-gradient(135deg,#fff2ee,#e65a4a)}
.link-text h3{font-size:12px;color:var(--text-blue);margin:2px 0 5px}
.link-text p{font-size:9.5px;line-height:1.6;color:var(--muted)}
.homepages{margin-top:22px;padding:0 10px}
.homepages h2{font-size:11px;font-weight:400;color:var(--ink);border-bottom:1px solid var(--line);padding-bottom:4px}
.homepage-logos{display:flex;gap:50px;padding:14px 16px 6px}
.homepage-logos .brand-mark{font-size:13px}
.homepage-logos .org{color:var(--ink);font-size:11px;margin-left:6px}
.site-footer{position:absolute;left:0;right:0;bottom:0;height:145px;background:var(--footer-blue);color:#fff}
.footer-links{display:flex;gap:26px;justify-content:flex-start;padding:12px 112px 0;font-size:9.5px}
.footer-links span::before{content:"▶";font-size:7px;margin-right:4px}
.footer-info{display:flex;gap:14px;padding:14px 112px 0;font-size:9px;line-height:1.6}
.footer-logo{display:flex;align-items:center;gap:5px;font-weight:700;font-size:13px;color:#fff}
.footer-logo::before{content:"";width:11px;height:11px;background:#fff}
.copyright{position:absolute;left:0;right:0;bottom:0;height:28px;line-height:28px;background:var(--footer-dark);text-align:center;font-size:9px}
</style>
</head>
<body>
<header class="site-header">
  <div class="brand">
    <span class="brand-mark">ハルタカ</span>
    <span class="brand-title">子育て支援 ポータルサイト</span>
  </div>
  <div class="header-tools">
    <div class="group-links"><span>ハルタカホールディングス</span><span>ハルタカ運輸</span></div>
    <div class="font-size">文字サイズ <b>小</b><b class="on">中</b><b>大</b></div>
  </div>
</header>

<section class="hero">
  <div class="hero-photo" role="img" aria-label="芝生の上で母親と子どもが寄り添って座る写真、背景に青空と木々"></div>
  <p class="hero-copy">ハルタカグループは<br>「子育て支援」を応援しています。</p>
</section>

<main class="content">
  <h2 class="section-title"><span>「子育て支援」リンク</span></h2>
  <ul class="link-list">
    <li class="link-item">
      <div class="link-banner b1" role="img" aria-label="ひよこノートのバナー"></div>
      <div class="link-text"><h3>ひよこノート</h3><p>妊娠・出産・育児の情報をまとめたサイトです。<br>毎日の子育てに役立つ記事をお届けします。<br>先輩ママの体験談も多数掲載しています。</p></div>
    </li>
    <li class="link-item">
      <div class="link-banner b2" role="img" aria-label="子育て支援施設のバナー"></div>
      <div class="link-text"><h3>子育て支援施設</h3><p>地域の子育て支援施設を紹介しています。<br>相談窓口や一時預かりの情報も探せます。<br>お近くの施設をぜひご利用ください。</p></div>
    </li>
    <li class="link-item">
      <div class="link-banner b3" role="img" aria-label="みんなの子育て応援会のバナー"></div>
      <div class="link-text"><h3>みんなの子育て応援会</h3><p>社会全体で子育てを応援する取り組みです。<br>活動の紹介やイベント情報を掲載中です。<br>応援の輪にぜひご参加ください。</p></div>
    </li>
    <li class="link-item">
      <div class="link-banner b4" role="img" aria-label="こども手帳ナビのバナー"></div>
      <div class="link-text"><h3>こども手帳ナビ</h3><p>子育てに関する制度や手当をまとめています。<br>申請方法や必要書類もわかりやすく解説。<br>困ったときの参考にしてください。</p></div>
    </li>
    <li class="link-item">
      <div class="link-banner b5" role="img" aria-label="のびのび子育てのバナー"></div>
      <div class="link-text"><h3>のびのび子育て</h3><p>子育ての悩みに専門家が答える番組です。<br>放送内容やおすすめ情報を紹介しています。<br>ご家族みんなでご覧ください。</p></div>
    </li>
  </ul>
  <div class="homepages">
    <h2>ホームページはこちら</h2>
    <div class="homepage-logos">
      <div class="brand-mark">ハルタカ<span class="org">ハルタカホールディングス</span></div>
      <div class="brand-mark">ハルタカ<span class="org">ハルタカ運輸</span></div>
    </div>
  </div>
</main>

<footer class="site-footer">
  <nav class="footer-links"><span>プライバシーポリシー</span><span>リンクポリシー</span><span>免責事項</span></nav>
  <div class="footer-info">
    <div class="footer-logo">ハルタカ</div>
    <p>お問い合わせ「子育て支援」係<br>〒500-0000 緑ヶ丘市中央町1丁目2番3号<br>TEL 0570-12-3456　FAX 0570-12-3457　E-mail info@hinata-nestlu.jp</p>
  </div>
  <div class="copyright">Copyright(c) 2016 harutaka-kosodate All Rights Reserved.</div>
</footer>
</body>
</html>
```